Halverin Link Group B.cards and Letterhead
B. cards
Professional
First Last
Executive
Amber Crest Tower
Office 5817
P.O.Box 6094
Jeddah 23867
Saudi Arabia
name@hlgnet.com
www.hlgnet.com
I want to print cards on pearl paper
either blank or a nice design or the logo

```html
<!DOCTYPE html>
<html lang="en">
<head>
<meta charset="utf-8">
<title>Halverin Link Group Stationery</title>
<link href="https://fonts.googleapis.com/css2?family=Open+Sans:wght@400;700&display=swap" rel="stylesheet">
<style>
:root{
  --bg:#eeeae4;
  --paper:#ffffff;
  --brand:#1f4fa3;
  --brand-dark:#123a80;
  --grey:#6d7074;
  --grey-dark:#4e5155;
  --text:#555a60;
  --faint:#eceef1;
  --caption:#8a8378;
}
*{margin:0;padding:0;box-sizing:border-box}
html,body{width:1200px;height:346px;overflow:hidden;background:var(--bg);font-family:"Open Sans",sans-serif;color:var(--text)}
.canvas{position:relative;width:1200px;height:346px}
.sheet{position:absolute;background:var(--paper);box-shadow:0 1px 3px rgba(0,0,0,.18)}
.brand-name{font-weight:700;color:var(--brand);white-space:nowrap;display:flex;align-items:center;gap:4px}
.brand-name .mark{display:inline-block;background:var(--brand);border-radius:50%}
.caption{position:absolute;font-size:4px;letter-spacing:.3px;text-transform:uppercase;color:var(--caption);white-space:nowrap}
.fine{font-size:3.6px;line-height:1.35}
.faint-disc{position:absolute;border-radius:50%;background:var(--faint)}

/* business cards */
.card-front{left:12px;top:130px;width:96px;height:42px;padding:5px}
.card-front .brand-name{font-size:6px}
.card-front .mark{width:5px;height:5px}
.card-front .person{margin-top:6px}
.card-back{left:12px;top:205px;width:96px;height:42px;display:flex;align-items:center;justify-content:center}
.card-back .brand-name{font-size:6.5px}
.card-back .mark{width:5px;height:5px}

/* letterheads */
.letterhead{top:12px;width:224px;height:318px}
.letterhead-one{left:137px}
.letterhead-two{left:374px}
.letterhead .brand-name{position:absolute;font-size:10px}
.letterhead .mark{width:8px;height:8px}
.letterhead-one .brand-name{left:18px;top:14px}
.letterhead-one .contact{position:absolute;right:16px;top:14px;text-align:right}
.letterhead-two .brand-name{left:50%;top:14px;transform:translateX(-50%)}
.letterhead .faint-disc{left:72px;top:150px;width:80px;height:80px}
.letterhead .footer{position:absolute;left:0;right:0;bottom:8px;text-align:center}

/* envelopes */
.envelope{left:619px;width:244px;height:90px}
.envelope-one{top:120px}
.envelope-two{top:240px}
.envelope .brand-name{position:absolute;left:10px;top:8px;font-size:7px}
.envelope .mark{width:6px;height:6px}
.envelope .return{position:absolute;left:10px;top:20px}

/* flap envelopes */
.flap-set{position:absolute;left:883px;top:12px;width:307px}
.flap{position:relative;width:307px;height:80px;overflow:hidden}
.flap svg{position:absolute;inset:0}
.flap .brand-name{position:absolute;left:50%;top:20px;transform:translateX(-50%);font-size:7px;color:var(--paper)}
.flap .mark{width:6px;height:6px;background:var(--paper)}
.flap-blue{background:var(--brand)}
.flap-grey{background:var(--grey)}
.flap-white{background:var(--paper);height:120px;box-shadow:0 1px 3px rgba(0,0,0,.18)}
</style>
</head>
<body>
<div class="canvas">

  <section class="sheet card-front">
    <div class="brand-name"><span class="mark"></span>Halverin Link Group</div>
    <div class="person fine">
      <strong>First Last</strong><br>Executive<br>name@hlgnet.com
    </div>
  </section>
  <span class="caption" style="left:12px;top:176px">business card</span>

  <section class="sheet card-back">
    <div class="brand-name"><span class="mark"></span>Halverin Link Group</div>
  </section>

  <section class="sheet letterhead letterhead-one">
    <div class="brand-name"><span class="mark"></span>Halverin Link Group</div>
    <div class="contact fine">
      Amber Crest Tower, Office 5817<br>
      P.O.Box 6094, Jeddah 23867<br>
      Saudi Arabia<br>
      www.hlgnet.com
    </div>
    <div class="faint-disc"></div>
    <div class="footer fine">www.hlgnet.com</div>
  </section>
  <span class="caption" style="left:210px;top:333px">letterhead design 1</span>

  <section class="sheet letterhead letterhead-two">
    <div class="brand-name"><span class="mark"></span>Halverin Link Group</div>
    <div class="faint-disc"></div>
    <div class="footer fine">Amber Crest Tower · Office 5817 · P.O.Box 6094 · Jeddah 23867 · www.hlgnet.com</div>
  </section>
  <span class="caption" style="left:448px;top:333px">letterhead design 2</span>

  <section class="sheet envelope envelope-one">
    <div class="brand-name"><span class="mark"></span>Halverin Link Group</div>
    <div class="return fine">Amber Crest Tower, Office 5817<br>P.O.Box 6094, Jeddah 23867</div>
  </section>
  <span class="caption" style="left:705px;top:213px">envelope design 1</span>

  <section class="sheet envelope envelope-two">
    <div class="brand-name"><span class="mark"></span>Halverin Link Group</div>
    <div class="return fine">Amber Crest Tower, Office 5817<br>P.O.Box 6094, Jeddah 23867</div>
  </section>
  <span class="caption" style="left:705px;top:333px">envelope design 2</span>

  <section class="flap-set">
    <div class="flap flap-blue">
      <svg viewBox="0 0 307 80" preserveAspectRatio="none"><polygon points="0,80 153,40 307,80" fill="var(--brand-dark)"/></svg>
      <div class="brand-name"><span class="mark"></span>Halverin Link Group</div>
    </div>
    <div class="flap flap-grey">
      <svg viewBox="0 0 307 80" preserveAspectRatio="none"><polygon points="0,80 153,40 307,80" fill="var(--grey-dark)"/></svg>
      <div class="brand-name"><span class="mark"></span>Halverin Link Group</div>
    </div>
    <div class="flap flap-white">
      <svg viewBox="0 0 307 120" preserveAspectRatio="none"><polyline points="0,0 153,60 307,0" fill="none" stroke="#dcdcdc" stroke-width="1"/></svg>
    </div>
  </section>
  <span class="caption" style="left:1000px;top:304px">envelope flap design</span>

</div>
</body>
</html>
```